Advertisement for a Digital Strategy Consultancy

We are 'PELICORN BRAANDA' a boutique agency that focuses on Digital Strategies for business. (i.e. online branding, social publicity stunts, viral advertising etc etc..)

We need a 30 second advertisement for the agency that says...

Holy crap dude... They look like they know what they are doing. Very simple and minimal tho...

Here is some inspiration:

http://portal.quilvanto.example/app/FullPlayer.aspx?id=a482917e-3b0c-472d-9e1f-77cbd0a3f109

Reason: We advertised the project as an advertisement when we are really chasing more of an animated slideshow

Reason: The project requires some planning that we feel justifies the amendment to the deadline.

Target Market(s)

Our target demographic is the typical 40+ year old that knows that in this day and age, he/she really should be putting more effort into the companies online marketing and advertising campaigns. BUT... Unfortunately for the company, somewhere along the way this person has like so many others, been convinced that instead of learning about what they are doing themselves, they should just pay some cheesy old man in a tracksuit to create them an bidlists campaign.

Industry/Entity Type

Advertising

Requirements
Must have
• Our url will be:

www.pelicornbraanda.example

The add must simply show the domain address somewhere/how?

Nice to have
• A high res version and a web optimised low res version of the ad
Should not have
• stolen ideas

```html
<!DOCTYPE html>
<html lang="en">
<head>
<meta charset="utf-8">
<title>Pelicorn Braanda — Digital Strategies storyboard</title>
<link rel="stylesheet" href="https://fonts.googleapis.com/css2?family=Crimson+Text:ital,wght@0,400;0,600;1,400&family=Arimo:wght@400&display=swap">
<style>
  :root {
    --page: #ffffff;
    --edge: #000000;
    --title-grey: #d6d6d6;
    --light-grey: #e8e8e8;
    --brand-red: #cc0000;
    --deep-red: #8a1010;
    --wine: #6a1212;
    --ink-dark: #2a2a2a;
    --dark-top: #1c1c1c;
    --dark-bottom: #353535;
    --pale-text: #bdbdbd;
    --logo-grey: #8c8c8c;
  }
  * { margin: 0; padding: 0; box-sizing: border-box; }
  html, body { width: 1200px; height: 900px; overflow: hidden; background: var(--page); }
  .board { position: relative; width: 1200px; height: 900px; font-family: "Crimson Text", Georgia, serif; }
  .edge-bar { position: absolute; right: 0; top: 0; width: 36px; height: 900px; background: var(--edge); }

  .frame { position: absolute; width: 300px; height: 224px; overflow: hidden; }
  .col-1 { left: 0; } .col-2 { left: 326px; } .col-3 { left: 652px; }
  .row-1 { top: 82px; } .row-2 { top: 354px; }
  .frame--title { background: var(--title-grey); }
  .frame--question { background: var(--light-grey); }
  .frame--dark { background: linear-gradient(180deg, var(--dark-top), var(--dark-bottom)); }

  .agency-name { position: absolute; left: 0; right: 0; top: 106px; text-align: center; color: var(--deep-red); font-size: 17px; letter-spacing: 0.5px; }
  .agency-url { position: absolute; left: 0; right: 0; top: 172px; text-align: center; color: var(--deep-red); font-size: 11px; }

  .question-mark { position: absolute; left: 0; top: 96px; width: 26px; height: 28px; background: var(--brand-red); }
  .question-text { position: absolute; left: 40px; top: 99px; color: var(--deep-red); font-size: 17px; white-space: nowrap; }
  .question-rule { position: absolute; left: 184px; top: 120px; width: 116px; height: 4px; background: var(--ink-dark); }

  .big-word { position: absolute; color: var(--pale-text); font-size: 128px; line-height: 1; white-space: nowrap; transform-origin: 0 0; }
  .big-word--tilted { left: 74px; top: -40px; transform: rotate(72deg) scaleY(0.8); }
  .big-word--faint { left: 74px; top: -40px; transform: rotate(72deg) scaleY(0.8); opacity: 0.22; }
  .side-word { position: absolute; left: 142px; top: -34px; writing-mode: vertical-rl; color: var(--pale-text); font-size: 34px; letter-spacing: 1px; }

  .red-shape { position: absolute; left: 0; top: 0; }

  .strategy-band { position: absolute; left: 140px; top: 0; width: 26px; background: var(--brand-red); display: flex; justify-content: center; }
  .strategy-band span { writing-mode: vertical-rl; color: #ffffff; font-family: "Arimo", Arial, sans-serif; font-size: 20px; padding-top: 14px; letter-spacing: 0.5px; }
  .band-full { height: 224px; }
  .band-short { height: 196px; }

  .bg-word { position: absolute; color: var(--wine); white-space: nowrap; opacity: 0.75; }
  .bg-publicity { left: 200px; top: 20px; font-size: 66px; opacity: 0.5; }
  .bg-bidlists { left: 2px; top: 104px; font-size: 20px; }
  .bg-fish { left: 76px; top: 94px; font-size: 30px; opacity: 0.55; }
  .bg-tactics { left: 170px; top: 114px; font-size: 36px; }

  .brand-mark { position: absolute; left: 800px; top: 772px; height: 56px; display: flex; align-items: center; gap: 12px; }
  .brand-square { width: 26px; height: 26px; background: var(--brand-red); }
  .brand-name { font-size: 40px; color: var(--logo-grey); line-height: 1; }
</style>
</head>
<body>
<main class="board">
  <section class="frame frame--title col-1 row-1">
    <p class="agency-name">PELICORN BRAANDA</p>
    <p class="agency-url">www.pelicornbraanda.example</p>
  </section>

  <section class="frame frame--title col-2 row-1">
    <p class="agency-name">PELICORN BRAANDA</p>
  </section>

  <section class="frame frame--question col-3 row-1">
    <div class="question-mark"></div>
    <p class="question-text">Want the best for your business?</p>
    <div class="question-rule"></div>
  </section>

  <section class="frame frame--dark col-1 row-2">
    <p class="big-word big-word--tilted">DIGITAL</p>
    <p class="side-word">STRATEGIES</p>
    <svg class="red-shape" width="300" height="224" viewBox="0 0 300 224" aria-hidden="true">
      <polygon points="0,172 168,188 180,224 0,224" fill="var(--brand-red)"/>
    </svg>
  </section>

  <section class="frame frame--dark col-2 row-2">
    <p class="bg-word bg-publicity">publicity</p>
    <p class="bg-word bg-fish">fish</p>
    <p class="bg-word bg-bidlists">bidlists</p>
    <p class="bg-word bg-tactics">tactics</p>
    <div class="strategy-band band-full"><span>STRATEGIES</span></div>
  </section>

  <section class="frame frame--dark col-3 row-2">
    <p class="big-word big-word--faint">DIGITAL</p>
    <svg class="red-shape" width="300" height="224" viewBox="0 0 300 224" aria-hidden="true">
      <polygon points="0,150 180,166 184,224 0,224" fill="var(--wine)" opacity="0.45"/>
    </svg>
    <div class="strategy-band band-short"><span>STRATEGIES</span></div>
  </section>

  <div class="brand-mark">
    <div class="brand-square"></div>
    <p class="brand-name">Pelicorn Braanda</p>
  </div>

  <div class="edge-bar"></div>
</main>
</body>
</html>
```